Webdesign für Seminaranbieter
Zielgruppe
Die Tessel Academy bietet Kurse, Seminare & Coachings im Bereich der Kommunikation / Persönlichkeitsentwicklung an.
Folgendes Angebot besteht zur Zeit:
Seminare:
- 'Erste Schritte Dialog', eine Einführung in die Kommunikation.
- 'Starke Familien, ruhige Abende' zum Thema Erziehung.
- 'Reife Jahre mit Gelassenheit', zum Thema Älter werden und den Umgang damit.
Kurse:
- 'Gewaltfreie Kommunikation', Übungsgruppe
Coaching:
- Einzelsitzungen mit Hypnose
Ps: im Anhang unter 'Angabot_Vorlage.pdf' finden Sie mehr Infos zu den einezlenen Angebote.
Aufgabenstellung
Bitte berücksichtigen Sie, dass bereits ein Logo besteht (siehe Anhang).
Vom gesamteindruck her sollte die Website aufgeräumt, übersichtlich, harmonisch, freundlich & frisch wirken.
Es wäre super, wenn die Website authentisch wirkt (und weniger '0815 Business Website').
Bitte bedenken Sie, dass die Website sich an Private richtet, die sich nach einem 'strahlenderen & unbeschwerterem Lebene sehnen'.
Wir haben bereits viele Persönlichkeiten stärken können und möchten dies auch witerhin mit viel Herzblut machen.

```html
<!DOCTYPE html>
<html lang="de">
<head>
<meta charset="utf-8">
<title>Tessel Academy – Neue Perspektiven</title>
<link rel="stylesheet" href="https://fonts.googleapis.com/css2?family=Montserrat:wght@400;500&display=swap">
<style>
  :root {
    --header-bg: #ece6dc;
    --nav-text: #4a4540;
    --nav-active: #e2582b;
    --brand-text: #2b2725;
    --hero-top: #e6d2b6;
    --hero-mid: #e4b98c;
    --hero-glow: #f7a14c;
    --hero-low: #a67f86;
    --hero-bottom: #6f5a7e;
    --hero-text: #ffffff;
  }
  * { margin: 0; padding: 0; box-sizing: border-box; }
  html, body {
    width: 1200px;
    height: 900px;
    overflow: hidden;
    font-family: "Montserrat", sans-serif;
  }
  .site {
    width: 1200px;
    height: 900px;
    display: flex;
    flex-direction: column;
  }
  .site-header {
    height: 110px;
    background: var(--header-bg);
    display: flex;
    align-items: center;
    justify-content: space-between;
    padding: 0 40px 0 50px;
  }
  .brand {
    display: flex;
    align-items: center;
    gap: 10px;
    color: var(--brand-text);
    font-size: 12px;
    font-weight: 500;
    letter-spacing: 2px;
    text-transform: uppercase;
  }
  .brand-dot {
    width: 9px;
    height: 9px;
    border-radius: 50%;
    background: var(--brand-text);
  }
  .main-nav ul {
    list-style: none;
    display: flex;
    gap: 28px;
    margin-top: -30px;
  }
  .main-nav a {
    color: var(--nav-text);
    text-decoration: none;
    font-size: 12px;
    letter-spacing: 0.5px;
    text-transform: uppercase;
  }
  .main-nav a.is-active {
    color: var(--nav-active);
    font-weight: 500;
  }
  .hero {
    position: relative;
    flex: 1;
  }
  .hero-photo {
    position: absolute;
    inset: 0;
    background:
      radial-gradient(ellipse 240px 190px at 72% 40%, rgba(247,161,76,0.95), rgba(247,161,76,0) 100%),
      radial-gradient(ellipse 420px 340px at 90% 48%, rgba(140,62,58,0.6), rgba(140,62,58,0) 100%),
      linear-gradient(180deg, var(--hero-top) 0%, var(--hero-mid) 42%, var(--hero-low) 76%, var(--hero-bottom) 100%);
  }
  .hero-copy {
    position: absolute;
    left: 0;
    right: 0;
    top: 170px;
    padding-left: 70px;
    text-align: center;
    color: var(--hero-text);
  }
  .hero-brand {
    font-size: 96px;
    font-weight: 400;
    letter-spacing: 6px;
    line-height: 1;
  }
  .hero-title {
    margin-top: 70px;
    font-size: 52px;
    font-weight: 400;
    letter-spacing: 8px;
    line-height: 1.1;
    text-transform: uppercase;
  }
  .hero-tagline {
    margin-top: 20px;
    font-size: 25px;
    font-weight: 400;
    letter-spacing: 2px;
    text-transform: uppercase;
  }
</style>
</head>
<body>
  <div class="site">
    <header class="site-header">
      <div class="brand">
        <span class="brand-dot"></span>
        <span class="brand-name">Tessel Academy</span>
      </div>
      <nav class="main-nav">
        <ul>
          <li><a href="#" class="is-active">Home</a></li>
          <li><a href="#">Über uns</a></li>
          <li><a href="#">Seminare</a></li>
          <li><a href="#">Kurse</a></li>
          <li><a href="#">Coaching</a></li>
          <li><a href="#">Kontakt</a></li>
        </ul>
      </nav>
    </header>
    <section class="hero">
      <div class="hero-photo" role="img" aria-label="Foto: Hände formen einen Rahmen um die untergehende Sonne über einer Berglandschaft"></div>
      <div class="hero-copy">
        <p class="hero-brand">Tessel</p>
        <h1 class="hero-title">Tessel Academy</h1>
        <p class="hero-tagline">Neue Perspectiven · Neue Horizonte</p>
      </div>
    </section>
  </div>
</body>
</html>
```